Business cards and stationary for construction company
Brackenfield Construction LLC
RT/KPN/OV Team
Hi, the font is. MicrogrammaDBolExt.
And the Construction llc is Helvetica.
Thanks
Hi contest holder, may I know the font used? Thank you.

```html
<!DOCTYPE html>
<html lang="en">
<head>
<meta charset="utf-8">
<title>Brackenfield Construction LLC — Business Card</title>
<link rel="stylesheet" href="https://fonts.googleapis.com/css2?family=Open+Sans:wght@400;600;700;800&display=swap">
<style>
  :root {
    --navy: #2f4775;
    --navy-deep: #243a63;
    --paper: #ffffff;
    --stage: #e9e7e3;
    --line-soft: rgba(255, 255, 255, 0.55);
  }
  html, body {
    margin: 0;
    padding: 0;
    width: 1200px;
    height: 900px;
    overflow: hidden;
    background: var(--stage);
    font-family: "Open Sans", Arial, sans-serif;
  }
  .canvas {
    position: relative;
    width: 1200px;
    height: 900px;
    display: flex;
    align-items: center;
    justify-content: center;
  }
  .business-card {
    position: relative;
    width: 1050px;
    height: 600px;
    background: var(--paper);
    box-shadow: 0 18px 40px rgba(0, 0, 0, 0.18);
    overflow: hidden;
  }
  .wave-band {
    position: absolute;
    inset: 0;
    width: 100%;
    height: 100%;
  }
  .brand-mark {
    position: absolute;
    top: 72px;
    left: 0;
    right: 0;
    text-align: center;
    color: var(--navy);
    font-weight: 800;
    line-height: 1;
  }
  .brand-name {
    display: block;
    font-size: 74px;
    letter-spacing: -1px;
  }
  .brand-tagline {
    display: block;
    margin-top: 8px;
    font-size: 22px;
    letter-spacing: 5px;
  }
  .contact-list {
    position: absolute;
    left: 48px;
    top: 378px;
    margin: 0;
    padding: 0;
    list-style: none;
    color: var(--paper);
    font-size: 24px;
    line-height: 1.25;
  }
  .contact-item {
    display: flex;
    align-items: center;
    gap: 10px;
    margin-bottom: 6px;
  }
  .contact-item.address-line {
    padding-left: 36px;
    margin-top: -4px;
  }
  .contact-icon {
    width: 26px;
    height: 26px;
    flex: none;
  }
  .signature-block {
    position: absolute;
    right: 48px;
    top: 356px;
    text-align: right;
    color: var(--paper);
  }
  .company-name {
    font-size: 28px;
    font-weight: 700;
    margin: 0;
  }
  .person-name {
    font-size: 22px;
    margin: 4px 0 0;
  }
</style>
</head>
<body>
<main class="canvas">
  <article class="business-card">
    <svg class="wave-band" viewBox="0 0 1050 600" aria-hidden="true">
      <path d="M0,345 C200,285 380,330 560,320 C760,308 900,230 1050,230 L1050,600 L0,600 Z" fill="var(--navy)"/>
      <path d="M0,318 C210,258 390,300 570,292 C770,282 910,205 1050,205" fill="none" stroke="var(--navy)" stroke-width="4"/>
      <path d="M0,372 C220,300 400,345 580,338 C780,330 915,255 1050,252" fill="none" stroke="var(--line-soft)" stroke-width="3"/>
      <path d="M0,395 C230,320 420,360 600,355 C790,350 920,275 1050,275" fill="none" stroke="var(--line-soft)" stroke-width="1.5"/>
      <path d="M0,360 C200,300 380,342 560,334 C760,322 900,245 1050,242" fill="none" stroke="var(--paper)" stroke-width="5"/>
    </svg>

    <div class="brand-mark">
      <span class="brand-name">Brackenfield</span>
      <span class="brand-tagline">CONSTRUCTION LLC</span>
    </div>

    <ul class="contact-list">
      <li class="contact-item">
        <svg class="contact-icon" viewBox="0 0 26 26" aria-hidden="true">
          <circle cx="13" cy="13" r="12" fill="var(--paper)"/>
          <path d="M7,13 L13,7.5 L19,13 M9,12 V18.5 H17 V12" fill="none" stroke="var(--navy)" stroke-width="2"/>
        </svg>
        <span>P.O. Box 612</span>
      </li>
      <li class="contact-item address-line"><span>Fairmont, OR 97411</span></li>
      <li class="contact-item">
        <svg class="contact-icon" viewBox="0 0 26 26" aria-hidden="true">
          <circle cx="13" cy="13" r="12" fill="var(--paper)"/>
          <rect x="9" y="6" width="8" height="14" rx="1.5" fill="none" stroke="var(--navy)" stroke-width="2"/>
          <circle cx="13" cy="17" r="1" fill="var(--navy)"/>
        </svg>
        <span>555-014-2290</span>
      </li>
      <li class="contact-item">
        <svg class="contact-icon" viewBox="0 0 26 26" aria-hidden="true">
          <circle cx="13" cy="13" r="12" fill="var(--paper)"/>
          <path d="M8,7 L11,7 L12,10.5 L10.3,11.8 C11.2,13.8 12.4,15 14.2,15.8 L15.5,14 L19,15 L19,18 C13,19 7,13 8,7 Z" fill="var(--navy)"/>
        </svg>
        <span>555-017-4481</span>
      </li>
      <li class="contact-item">
        <svg class="contact-icon" viewBox="0 0 26 26" aria-hidden="true">
          <circle cx="13" cy="13" r="12" fill="var(--paper)"/>
          <rect x="6.5" y="8.5" width="13" height="9" fill="none" stroke="var(--navy)" stroke-width="1.8"/>
          <path d="M6.5,8.5 L13,13.5 L19.5,8.5" fill="none" stroke="var(--navy)" stroke-width="1.8"/>
        </svg>
        <span>brackenfield@isp.com</span>
      </li>
      <li class="contact-item">
        <svg class="contact-icon" viewBox="0 0 26 26" aria-hidden="true">
          <circle cx="13" cy="13" r="12" fill="var(--paper)"/>
          <circle cx="13" cy="13" r="6.5" fill="none" stroke="var(--navy)" stroke-width="1.6"/>
          <ellipse cx="13" cy="13" rx="2.8" ry="6.5" fill="none" stroke="var(--navy)" stroke-width="1.4"/>
          <path d="M6.5,13 H19.5" stroke="var(--navy)" stroke-width="1.4"/>
        </svg>
        <span>www.brackenfield@isp.com</span>
      </li>
    </ul>

    <div class="signature-block">
      <p class="company-name">Brackenfield Construction LLC</p>
      <p class="person-name">Dana R. Holloway</p>
    </div>
  </article>
</main>
</body>
</html>
```